Artisan Bread Company needs a business card

I need a business card design, for an artisan bread company called "Hollin's Bread".

I would like the logo on one side, and on the other, I would like it to say

Tavish Hollin
Baker
519.362.4175
hollinsbread@mailvexo.com

Not necessarily in that order- but it must have these.

Industry/Entity Type

Business

Font styles to use
Serif

Requirements
Must have
• The provided logo on the front, this on the back-
• Tavish Hollin
• Baker
• 519.362.4175
• hollinsbread@mailvexo.com

```html
<!DOCTYPE html>
<html lang="en">
<head>
<meta charset="utf-8">
<title>Hollin's Bread — Business Card</title>
<link rel="stylesheet" href="https://fonts.googleapis.com/css2?family=Didact+Gothic&family=Pinyon+Script&display=swap">
<style>
  :root {
    --backdrop: #d4d4d4;
    --kraft: #e3d3b3;
    --ink: #1c1a17;
  }
  * { box-sizing: border-box; margin: 0; padding: 0; }
  html, body {
    width: 1200px;
    height: 1004px;
    overflow: hidden;
    background: var(--backdrop);
  }
  .sheet {
    width: 1200px;
    height: 1004px;
    display: flex;
    flex-direction: column;
    align-items: center;
    justify-content: center;
    gap: 60px;
  }
  .card {
    width: 580px;
    height: 340px;
    background: var(--kraft);
    color: var(--ink);
    position: relative;
    box-shadow: 0 6px 14px rgba(0, 0, 0, 0.18);
  }
  .card--front {
    display: flex;
    align-items: center;
    justify-content: center;
  }
  .wordmark {
    font-family: "Didact Gothic", sans-serif;
    font-weight: 400;
    color: var(--ink);
    text-align: center;
    line-height: 1.1;
    letter-spacing: 0.04em;
  }
  .wordmark--large { font-size: 46px; }
  .wordmark--small {
    position: absolute;
    left: 62px;
    top: 150px;
    font-size: 27px;
  }
  .contact {
    position: absolute;
    left: 310px;
    top: 122px;
  }
  .contact__name {
    font-family: "Pinyon Script", cursive;
    font-size: 27px;
    line-height: 1;
  }
  .contact__role {
    font-family: "Didact Gothic", sans-serif;
    font-size: 13px;
    margin: 8px 0 12px;
  }
  .contact__line {
    display: flex;
    align-items: center;
    gap: 10px;
    font-family: "Didact Gothic", sans-serif;
    font-size: 14px;
    margin-bottom: 5px;
  }
  .contact__icon { width: 13px; height: 13px; flex: none; }
</style>
</head>
<body>
  <main class="sheet">
    <section class="card card--front" aria-label="Card front">
      <p class="wordmark wordmark--large">Hollin's Bread</p>
    </section>

    <section class="card card--back" aria-label="Card back">
      <p class="wordmark wordmark--small">Hollin's Bread</p>
      <div class="contact">
        <p class="contact__name">Tavish Hollin</p>
        <p class="contact__role">Baker</p>
        <p class="contact__line">
          <svg class="contact__icon" viewBox="0 0 16 16" aria-hidden="true">
            <path fill="var(--ink)" d="M2 5c0-2 2-3 6-3s6 1 6 3v1h-3V5H5v1H2z M4 7h8l2 6H2z"/>
            <circle cx="8" cy="10" r="1.6" fill="var(--kraft)"/>
          </svg>
          519.362.4175
        </p>
        <p class="contact__line">
          <svg class="contact__icon" viewBox="0 0 16 16" aria-hidden="true">
            <rect x="1" y="3" width="14" height="10" fill="var(--ink)"/>
            <path d="M1.5 3.5 8 9l6.5-5.5" fill="none" stroke="var(--kraft)" stroke-width="1.2"/>
          </svg>
          hollinsbread@mailvexo.com
        </p>
      </div>
    </section>
  </main>
</body>
</html>
```